Stylish Homeware business needs a Logo and Business Card design

We need a logo and business card for a new company based in Hong Kong called "Nest Lumora". We do marketing and distributing international curated living goods for Asian homes. Products we handle included clocks, picture frame, small kitchen wares, LED lightenings, stationary and etc. We planned to also create our own brands next step. We could like to see designs that use pastel colors. The final design shoudl be simple and stylish.
Target Market(s)
Asia, Mainly Japan, China and Korea
Industry/Entity Type
Business
Contact Information for Business Card
We could like to see designs that use pastel colors. The final design shoudl be simple and stylish. We attach some log design we like on the bottom of the page.
Font styles to use
Look and feel
Each slider illustrates characteristics of the customer's brand and the style your logo design should communicate.

```html
<!DOCTYPE html>
<html lang="en">
<head>
<meta charset="UTF-8">
<title>Nest Lumora – Business Card</title>
<link rel="stylesheet" href="https://fonts.googleapis.com/css2?family=Roboto:wght@400;500;700&display=swap">
<style>
  :root {
    --page-bg: #e9e6e1;
    --card-bg: #0d0d0f;
    --brand-blue: #7f8fd6;
    --accent-orange: #f28a2e;
    --text-white: #f4f4f4;
    --text-soft: #d6d6d6;
  }
  * { margin: 0; padding: 0; box-sizing: border-box; }
  html, body {
    width: 900px; height: 1200px; overflow: hidden;
    background: var(--page-bg);
    font-family: "Roboto", Arial, sans-serif;
  }
  .canvas { position: relative; width: 900px; height: 1200px; }
  .card {
    position: absolute; left: 90px; width: 720px;
    background: var(--card-bg); border-radius: 24px;
    box-shadow: 0 10px 28px rgba(0,0,0,0.25);
    color: var(--text-white);
  }
  .card-front { top: 150px; height: 430px; }
  .card-back { top: 640px; height: 410px; }

  .brand { position: absolute; display: flex; align-items: center; gap: 16px; }
  .brand-dot { width: 60px; height: 60px; border-radius: 50%; background: var(--accent-orange); flex: none; }
  .brand-name {
    font-weight: 500; font-size: 46px; letter-spacing: 0.5px;
    color: var(--brand-blue); text-transform: uppercase; line-height: 1;
    white-space: nowrap;
  }
  .brand-tagline {
    font-size: 21px; color: var(--text-soft); margin-top: 6px; line-height: 1.1;
    white-space: nowrap;
  }

  .card-front .brand { top: 54px; left: 160px; }

  .person { position: absolute; left: 42px; top: 228px; }
  .person-name { font-size: 25px; font-weight: 700; letter-spacing: 0.5px; }
  .person-title { font-size: 16px; color: var(--brand-blue); margin-top: 4px; }

  .contact-list { position: absolute; left: 42px; top: 300px; list-style: none; }
  .contact-list li {
    display: flex; align-items: center; gap: 12px;
    font-size: 16px; color: var(--text-soft); height: 24px;
  }
  .contact-icon { width: 15px; height: 15px; flex: none; }

  .address {
    position: absolute; right: 40px; top: 370px;
    font-size: 16px; color: var(--text-soft);
  }

  .card-back .brand {
    left: 0; right: 0; top: 120px;
    flex-direction: column; gap: 14px; text-align: center;
  }
  .card-back .brand-name { font-size: 44px; }
  .card-back .brand-tagline { font-size: 20px; margin-top: -6px; }
</style>
</head>
<body>
<main class="canvas">

  <section class="card card-front" aria-label="Business card front">
    <div class="brand">
      <span class="brand-dot"></span>
      <div>
        <div class="brand-name">Nest Lumora</div>
        <div class="brand-tagline">curated living goods for Asian homes</div>
      </div>
    </div>

    <div class="person">
      <div class="person-name">DANIEL REYES</div>
      <div class="person-title">Director Operations</div>
    </div>

    <ul class="contact-list">
      <li>
        <svg class="contact-icon" viewBox="0 0 16 16"><rect x="1" y="2" width="14" height="12" rx="2" fill="none" stroke="#d6d6d6" stroke-width="1.6"/><rect x="4" y="5" width="8" height="3" fill="#d6d6d6"/></svg>
        031-208-617
      </li>
      <li>
        <svg class="contact-icon" viewBox="0 0 16 16"><path d="M3 1.5l3 .5 1 3.5-2 1.2a9 9 0 0 0 4.3 4.3l1.2-2 3.5 1 .5 3c-1 1-2.5 1.5-4 1A12 12 0 0 1 1.5 5.5c-.5-1.5 0-3 1.5-4z" fill="#d6d6d6"/></svg>
        852-915-406
      </li>
      <li>
        <svg class="contact-icon" viewBox="0 0 16 16"><rect x="1" y="3" width="14" height="10" rx="1.5" fill="#f28a2e"/><path d="M1.5 4l6.5 5 6.5-5" fill="none" stroke="#0d0d0f" stroke-width="1.4"/></svg>
        daniel@nestlumora.com
      </li>
      <li>
        <svg class="contact-icon" viewBox="0 0 16 16"><circle cx="8" cy="8" r="6.5" fill="none" stroke="#d6d6d6" stroke-width="1.4"/><ellipse cx="8" cy="8" rx="2.8" ry="6.5" fill="none" stroke="#d6d6d6" stroke-width="1.2"/><path d="M1.5 8h13" stroke="#d6d6d6" stroke-width="1.2"/></svg>
        www.nestlumora.com
      </li>
    </ul>

    <div class="address">18 Harbour Lane, Kowloon 00852</div>
  </section>

  <section class="card card-back" aria-label="Business card back">
    <div class="brand">
      <span class="brand-dot"></span>
      <div class="brand-name">Nest Lumora</div>
      <div class="brand-tagline">curated living goods for Asian homes</div>
    </div>
  </section>

</main>
</body>
</html>
```